Securities Exam Training Banner Add for Promoline campaign

We need a banner ad design to use for a remarketing campaign in Fennic Promoline. We are a securities exam training provider that provides online training across the U.S. and Canada. Banner ad designs should be consistent in color and concept with our website: www.brevanlearnhub.example.

Approved ad copy:

"Pass on your first attempt. Experience what you are missing with your current training provider."

"Pass the Tier 4 on your first attempt with our industry-leading training program. "

-High quality audio lecture.
-Interactive visual presentations.
-Comprehensive course textbook.

"We give you everything you need to pass on your first attempt."

Deliverables:

-Ad Sizes (250x250; 200x200; 468x60; 728x90; 300x250; 336x280; 120x600; 160x600)
-.gif, .jpg, .png, or .swf
-50kb or smaller

Theme:

-Design should reflect financial security, confidence in the product, and differentiation from the "rest of the industry."

Target Market(s)

People who are training for securities exams in the financial industry. e.g. people who work for Dorrance Pell, Hadley Fenwick, Corvin Tate, etc..

Industry/Entity Type

Financial

Requirements
Must have
• Company Logo and phrase "The leader in securities exam prep"
Strong call to action on final screen (Buy Now).

```html
<!DOCTYPE html>
<html lang="en">
<head>
<meta charset="utf-8">
<title>Brevan Learnhub – Securities Exam Prep Banner Set</title>
<link rel="stylesheet" href="https://fonts.googleapis.com/css2?family=Bebas+Neue&family=Lato:wght@400;700&display=swap">
<style>
  :root {
    --stage: #33312e;
    --blue-deep: #0a3494;
    --blue-mid: #1356c4;
    --blue-light: #2a7de6;
    --white: #ffffff;
    --yellow-top: #ffd43a;
    --yellow-bottom: #f59c00;
    --button-edge: #d98a00;
    --ink: #1a1a1a;
    --logo-grey: #4a4d52;
    --logo-mark: #1d4fae;
    --tick: #ffc51f;
    --photo-a: #6f86b8;
    --photo-b: #20306a;
  }
  * { box-sizing: border-box; margin: 0; padding: 0; }
  html, body { width: 1200px; height: 848px; overflow: hidden; }
  body { background: var(--stage); position: relative; font-family: "Lato", Arial, sans-serif; }

  .banner { position: absolute; background: var(--white); overflow: hidden; }
  .banner__field {
    position: absolute; left: 0; top: 0;
    background: radial-gradient(ellipse at 70% 30%, var(--blue-light) 0%, var(--blue-mid) 45%, var(--blue-deep) 100%);
  }
  .banner__photo {
    position: absolute;
    background: linear-gradient(160deg, var(--photo-a) 0%, #3d528f 55%, var(--photo-b) 100%);
  }
  .headline { position: absolute; z-index: 2; font-family: "Bebas Neue", "Arial Narrow", sans-serif; font-weight: 400; line-height: 0.92; color: var(--white); text-shadow: 0 2px 3px rgba(0,0,0,.45); white-space: nowrap; }
  .headline__accent { color: var(--yellow-top); display: block; }
  .headline__line { display: block; }

  .features { position: absolute; z-index: 2; list-style: none; color: var(--white); }
  .features li { position: relative; padding-left: 1.05em; }
  .features li::before { content: "✓"; position: absolute; left: 0; top: 0; color: var(--tick); font-weight: 700; }
  .features--single li { white-space: nowrap; }

  .logo { position: absolute; display: flex; align-items: center; gap: 6px; }
  .logo__mark { background: var(--logo-mark); flex: none; }
  .logo__name { font-family: "Lato", Arial, sans-serif; font-weight: 400; color: var(--logo-grey); text-transform: uppercase; line-height: 0.95; letter-spacing: 0.02em; white-space: nowrap; }

  .buy-now {
    position: absolute; display: flex; align-items: center; justify-content: center; gap: 10px;
    background: linear-gradient(var(--yellow-top), var(--yellow-bottom));
    border: 1px solid var(--button-edge); border-radius: 5px;
    font-family: "Lato", Arial, sans-serif; font-weight: 700; color: var(--ink);
    box-shadow: 0 2px 3px rgba(0,0,0,.3); white-space: nowrap;
  }
  .buy-now__arrow { flex: none; }

  .notch-up { position: absolute; width: 0; height: 0; border-left: 9px solid transparent; border-right: 9px solid transparent; border-bottom: 12px solid var(--white); }
  .notch-left { position: absolute; width: 0; height: 0; border-top: 9px solid transparent; border-bottom: 9px solid transparent; border-right: 12px solid var(--white); }

  /* 160x600 skyscraper */
  .sky { left: 56px; top: 67px; width: 195px; height: 732px; }
  .sky .banner__field { width: 195px; height: 598px; }
  .sky .headline { left: 9px; top: 16px; font-size: 42px; }
  .sky .headline__accent { font-size: 45px; }
  .sky .features { left: 12px; top: 168px; width: 180px; font-size: 19px; line-height: 1.12; }
  .sky .features li { margin-bottom: 10px; }
  .sky .banner__photo { left: 29px; top: 350px; width: 160px; height: 248px; }
  .sky .notch-up { left: 14px; top: 586px; }
  .sky .logo { left: 10px; top: 620px; }
  .sky .logo__mark { width: 32px; height: 32px; }
  .sky .logo__name { font-size: 16px; }
  .sky .buy-now { left: 10px; top: 675px; width: 174px; height: 46px; font-size: 22px; }

  /* 336x280 rectangle */
  .rect-lg { left: 276px; top: 67px; width: 410px; height: 341px; }
  .rect-lg .banner__field { width: 410px; height: 268px; }
  .rect-lg .headline { left: 10px; top: 12px; font-size: 50px; }
  .rect-lg .headline__accent { font-size: 56px; }
  .rect-lg .features { left: 10px; top: 164px; font-size: 17px; line-height: 1.65; }
  .rect-lg .banner__photo { left: 294px; top: 0; width: 116px; height: 268px; }
  .rect-lg .notch-up { left: 14px; top: 256px; }
  .rect-lg .logo { left: 12px; top: 288px; }
  .rect-lg .logo__mark { width: 36px; height: 36px; }
  .rect-lg .logo__name { font-size: 18px; }
  .rect-lg .buy-now { left: 222px; top: 285px; width: 176px; height: 45px; font-size: 21px; }

  /* 300x250 rectangle */
  .rect-md { left: 710px; top: 67px; width: 364px; height: 305px; }
  .rect-md .banner__field { width: 364px; height: 244px; }
  .rect-md .headline { left: 9px; top: 10px; font-size: 45px; }
  .rect-md .headline__accent { font-size: 50px; }
  .rect-md .features { left: 9px; top: 146px; font-size: 15px; line-height: 1.6; }
  .rect-md .banner__photo { left: 264px; top: 0; width: 100px; height: 244px; }
  .rect-md .notch-up { left: 12px; top: 232px; }
  .rect-md .logo { left: 12px; top: 258px; }
  .rect-md .logo__mark { width: 34px; height: 34px; }
  .rect-md .logo__name { font-size: 16.5px; }
  .rect-md .buy-now { left: 198px; top: 255px; width: 155px; height: 42px; font-size: 20px; }

  /* 468x60 banner */
  .board-sm { left: 435px; top: 552px; width: 571px; height: 71px; }
  .board-sm .banner__field { width: 450px; height: 71px; }
  .board-sm .banner__photo { left: 0; top: 0; width: 66px; height: 71px; }
  .board-sm .headline { left: 72px; top: 10px; font-size: 30px; line-height: 0.85; }
  .board-sm .headline__accent { font-size: 20px; margin-top: 3px; }
  .board-sm .features { left: 252px; top: 6px; font-size: 11.5px; line-height: 1.6; }
  .board-sm .notch-left { left: 438px; top: 26px; }
  .board-sm .logo { left: 458px; top: 8px; gap: 4px; }
  .board-sm .logo__mark { width: 20px; height: 20px; }
  .board-sm .logo__name { font-size: 10px; }
  .board-sm .buy-now { left: 466px; top: 38px; width: 94px; height: 24px; font-size: 12px; gap: 6px; border-radius: 3px; }

  /* 728x90 leaderboard */
  .board-lg { left: 276px; top: 641px; width: 889px; height: 110px; }
  .board-lg .banner__field { width: 700px; height: 110px; }
  .board-lg .banner__photo { left: 0; top: 0; width: 100px; height: 110px; }
  .board-lg .headline { left: 110px; top: 14px; font-size: 50px; line-height: 0.88; }
  .board-lg .headline__accent { font-size: 32px; margin-top: 5px; }
  .board-lg .features { left: 378px; top: 11px; font-size: 19px; line-height: 1.55; }
  .board-lg .notch-left { left: 688px; top: 46px; }
  .board-lg .logo { left: 712px; top: 14px; }
  .board-lg .logo__mark { width: 32px; height: 32px; }
  .board-lg .logo__name { font-size: 16px; }
  .board-lg .buy-now { left: 723px; top: 58px; width: 150px; height: 40px; font-size: 19px; }
</style>
</head>
<body>

<section class="banner sky" aria-label="160 by 600 skyscraper">
  <div class="banner__field"></div>
  <h2 class="headline"><span class="headline__line">The Leader</span><span class="headline__line">in Securities</span><span class="headline__accent">Exam Prep</span></h2>
  <ul class="features"><li>High quality audio lecture.</li><li>Interactive visual presentations.</li><li>Comprehensive course textbook.</li></ul>
  <div class="banner__photo" role="img" aria-label="Photo of a smiling businesswoman holding a blue clipboard"></div>
  <span class="notch-up"></span>
  <div class="logo"><span class="logo__mark"></span><span class="logo__name">Brevan<br>Learnhub</span></div>
  <a class="buy-now">Buy Now <svg class="buy-now__arrow" width="26" height="26" viewBox="0 0 26 26"><circle cx="13" cy="13" r="12" fill="#222"/><path d="M10 7l6 6-6 6" stroke="#fff" stroke-width="3" fill="none"/></svg></a>
</section>

<section class="banner rect-lg" aria-label="336 by 280 rectangle">
  <div class="banner__field"></div>
  <div class="banner__photo" role="img" aria-label="Photo of a smiling businesswoman holding a blue clipboard"></div>
  <h2 class="headline"><span class="headline__line">The Leader</span><span class="headline__line">in Securities</span><span class="headline__accent">Exam Prep</span></h2>
  <ul class="features features--single"><li>High quality audio lecture.</li><li>Interactive visual presentations.</li><li>Comprehensive course textbook.</li></ul>
  <span class="notch-up"></span>
  <div class="logo"><span class="logo__mark"></span><span class="logo__name">Brevan<br>Learnhub</span></div>
  <a class="buy-now">Buy Now <svg class="buy-now__arrow" width="26" height="26" viewBox="0 0 26 26"><circle cx="13" cy="13" r="12" fill="#222"/><path d="M10 7l6 6-6 6" stroke="#fff" stroke-width="3" fill="none"/></svg></a>
</section>

<section class="banner rect-md" aria-label="300 by 250 rectangle">
  <div class="banner__field"></div>
  <div class="banner__photo" role="img" aria-label="Photo of a smiling businesswoman holding a blue clipboard"></div>
  <h2 class="headline"><span class="headline__line">The Leader</span><span class="headline__line">in Securities</span><span class="headline__accent">Exam Prep</span></h2>
  <ul class="features features--single"><li>High quality audio lecture.</li><li>Interactive visual presentations.</li><li>Comprehensive course textbook.</li></ul>
  <span class="notch-up"></span>
  <div class="logo"><span class="logo__mark"></span><span class="logo__name">Brevan<br>Learnhub</span></div>
  <a class="buy-now">Buy Now <svg class="buy-now__arrow" width="24" height="24" viewBox="0 0 26 26"><circle cx="13" cy="13" r="12" fill="#222"/><path d="M10 7l6 6-6 6" stroke="#fff" stroke-width="3" fill="none"/></svg></a>
</section>

<section class="banner board-sm" aria-label="468 by 60 banner">
  <div class="banner__field"></div>
  <div class="banner__photo" role="img" aria-label="Photo of a smiling businesswoman holding a blue clipboard"></div>
  <h2 class="headline"><span class="headline__line">The Leader In</span><span class="headline__accent">Securities Exam Prep</span></h2>
  <ul class="features features--single"><li>High quality audio lecture.</li><li>Interactive visual presentations.</li><li>Comprehensive course textbook.</li></ul>
  <span class="notch-left"></span>
  <div class="logo"><span class="logo__mark"></span><span class="logo__name">Brevan<br>Learnhub</span></div>
  <a class="buy-now">Buy Now <svg class="buy-now__arrow" width="15" height="15" viewBox="0 0 26 26"><circle cx="13" cy="13" r="12" fill="#222"/><path d="M10 7l6 6-6 6" stroke="#fff" stroke-width="3" fill="none"/></svg></a>
</section>

<section class="banner board-lg" aria-label="728 by 90 leaderboard">
  <div class="banner__field"></div>
  <div class="banner__photo" role="img" aria-label="Photo of a smiling businesswoman holding a blue clipboard"></div>
  <h2 class="headline"><span class="headline__line">The Leader In</span><span class="headline__accent">Securities Exam Prep</span></h2>
  <ul class="features features--single"><li>High quality audio lecture.</li><li>Interactive visual presentations.</li><li>Comprehensive course textbook.</li></ul>
  <span class="notch-left"></span>
  <div class="logo"><span class="logo__mark"></span><span class="logo__name">Brevan<br>Learnhub</span></div>
  <a class="buy-now">Buy Now <svg class="buy-now__arrow" width="24" height="24" viewBox="0 0 26 26"><circle cx="13" cy="13" r="12" fill="#222"/><path d="M10 7l6 6-6 6" stroke="#fff" stroke-width="3" fill="none"/></svg></a>
</section>

</body>
</html>
```